Book cover - Quiet Rooms, Open Doors

Book cover for Ebook (Pagelight) and wrap around print cover (Printvale) (back, front, and spine)

The book title (may slightly change by end of brief):
(MAIN TITLE) 'Quiet Rooms, Open Doors'
(SUB HEADING) 'A Week-by-Week Practical Workbook to Loosen Nervous Habits, Quieten Doubt and Build Steady Poise'
by Dr Owen Hartley

I would like a bold, stand out cover. Contemporary. I would like to avoid stereotypical images of people looking anxious or worried. I would like the design to be more uplifting and hopeful, rather than focusing on the negative aspect of anxiety, but avoiding cliched photos of people raising their hands in the air, smiling and jumping etc. The cover should appeal to both men and women.

Trim size of book cover (for PrintVale) is 5.25" x 8" back and front with a spine size of 0.477 inches

Reason: I have decided to extend the deadline by 1 more day, not because I am unhappy with the quality of the designs, but because a few designers have contacted me to explain they have had technical difficulties when submitting their files. Thanks everyone for the hard work and great designs.

Target Market(s)

Males and females (16+) who struggle with social anxiety and shyness

Industry/Entity Type

Social

Font styles to use
Serif

Requirements
Must have
• Bold cover that is modern and contemporary. For example, I like these covers:
• http://shrtlnk.example/k4Tq9Zb
• http://shrtlnk.example/m8Wv2Hn
• http://shrtlnk.example/p3Jx6Lr
• http://shrtlnk.example/t7Gd1Qe
• http://shrtlnk.example/v2Nk8Fy
• http://shrtlnk.example/w9Bh4Cs
• http://shrtlnk.example/z5Mf3Ud
Nice to have
• Open to abstract designs.
Should not have
• No stereotypical pictures of people who look anxious or worried. Avoid cliched photos of people raising their hands in the air, smiling and jumping etc.

```html
<!DOCTYPE html>
<html lang="en">
<head>
<meta charset="utf-8">
<title>Quiet Rooms, Open Doors — Front Cover</title>
<link rel="stylesheet" href="https://fonts.googleapis.com/css2?family=Jost:wght@300;400&display=swap">
<style>
  :root {
    --backdrop: #ececec;
    --paper: #fcf4ee;
    --title-red: #a8141c;
    --ink: #141414;
    --disc: #ffffff;
    --tone-warm: #f6a04a;
    --tone-mid: #d873c8;
    --tone-cool: #dde878;
  }
  * { margin: 0; padding: 0; box-sizing: border-box; }
  html, body {
    width: 1200px;
    height: 900px;
    overflow: hidden;
    background: var(--backdrop);
  }
  .canvas {
    position: relative;
    width: 1200px;
    height: 900px;
    display: flex;
    justify-content: center;
    align-items: center;
  }
  .cover {
    position: relative;
    width: 600px;
    height: 900px;
    background: var(--paper);
    overflow: hidden;
    font-family: 'Jost', 'Futura', sans-serif;
  }
  .cover__artwork {
    position: absolute;
    inset: 0;
    width: 100%;
    height: 100%;
  }
  .cover__disc {
    position: absolute;
    left: 95px;
    top: 185px;
    width: 410px;
    height: 410px;
    border-radius: 50%;
    background: var(--disc);
    display: flex;
    flex-direction: column;
    align-items: center;
    justify-content: center;
    text-align: center;
    padding: 0 40px;
  }
  .cover__title {
    font-weight: 300;
    text-transform: uppercase;
    line-height: 1.02;
  }
  .cover__title-lead {
    display: block;
    color: var(--title-red);
    font-size: 46px;
    letter-spacing: 0.01em;
  }
  .cover__title-rest {
    display: block;
    color: var(--ink);
    font-size: 44px;
    margin-top: 4px;
  }
  .cover__subtitle {
    margin-top: 22px;
    max-width: 270px;
    font-weight: 400;
    font-size: 13.5px;
    line-height: 1.25;
    color: var(--ink);
  }
  .cover__author {
    position: absolute;
    left: 0;
    right: 0;
    bottom: 72px;
    text-align: center;
    font-weight: 400;
    font-size: 23px;
    letter-spacing: 0.42em;
    text-transform: uppercase;
    color: var(--ink);
  }
</style>
</head>
<body>
<main class="canvas">
  <article class="cover">
    <svg class="cover__artwork" viewBox="0 0 600 900" role="img"
         aria-label="Area for an abstract colour wash artwork behind the title">
      <defs>
        <linearGradient id="wash-tones" x1="0" y1="0" x2="0" y2="1">
          <stop offset="0" stop-color="var(--tone-warm)"/>
          <stop offset="0.5" stop-color="var(--tone-mid)"/>
          <stop offset="1" stop-color="var(--tone-cool)"/>
        </linearGradient>
      </defs>
      <rect x="40" y="60" width="520" height="700" rx="40" fill="url(#wash-tones)" opacity="0.55"/>
    </svg>

    <div class="cover__disc">
      <h1 class="cover__title">
        <span class="cover__title-lead">Quiet Rooms,</span>
        <span class="cover__title-rest">Open Doors</span>
      </h1>
      <p class="cover__subtitle">A Week-by-Week Practical Workbook to Loosen Nervous Habits, Quieten Doubt and Build Steady Poise</p>
    </div>

    <p class="cover__author">Dr Owen Hartley</p>
  </article>
</main>
</body>
</html>
```